Facebook and Instagram advertisement

Design a Facebook/Instagram ad using the attached file and info from our website. Please exclude the $69.99 BASIC package.
Our website is www.tallowbrookmedia.com

```html
<!DOCTYPE html>
<html lang="en">
<head>
<meta charset="utf-8">
<title>Tallowbrook Media – Internet Ultra</title>
<link href="https://fonts.googleapis.com/css2?family=Bebas+Neue&family=Montserrat:wght@500;600;700;800&display=swap" rel="stylesheet">
<style>
  :root {
    --red: #e8192c;
    --navy: #0b2d5b;
    --blue: #1a8fd0;
    --cyan: #4cc6de;
    --white: #ffffff;
    --sky-top: #081640;
    --sky-mid: #123a6e;
    --body-text: #1d2d4a;
  }
  * { margin: 0; padding: 0; box-sizing: border-box; }
  html, body { width: 960px; height: 1200px; overflow: hidden; background: var(--white); }
  .ad {
    position: relative;
    width: 960px;
    height: 1200px;
    overflow: hidden;
    background: var(--white);
    font-family: "Montserrat", Arial, sans-serif;
  }
  .sky {
    position: absolute;
    left: 0; top: 0;
    width: 960px; height: 620px;
    background:
      radial-gradient(ellipse 420px 160px at 560px 330px, rgba(60,190,180,0.75), transparent 70%),
      radial-gradient(ellipse 300px 120px at 180px 300px, rgba(40,150,160,0.55), transparent 70%),
      linear-gradient(180deg, var(--sky-top) 0%, var(--sky-mid) 45%, #173f5c 75%, #0d2236 100%);
  }
  .waves { position: absolute; left: 0; top: 0; }
  .display {
    position: absolute;
    font-family: "Bebas Neue", "Oswald", sans-serif;
    line-height: 1;
    white-space: nowrap;
  }
  .headline-internet { left: 158px; top: 79px; font-size: 62px; color: var(--white); }
  .headline-ultra { left: 156px; top: 118px; font-size: 180px; color: var(--white); letter-spacing: -2px; }
  .headline-speed { left: 491px; top: 136px; font-size: 50px; color: var(--white); }
  .headline-mbps { left: 490px; top: 174px; font-size: 107px; color: var(--white); }

  .plan-ring { position: absolute; left: 50px; }
  .plan-ring.premium { top: 340px; }
  .plan-ring.basic { top: 688px; }

  .plan-price { font-size: 86px; color: var(--red); left: 164px; }
  .plan-price .cents { font-size: 46px; }
  .plan-term { font-size: 69px; color: var(--red); left: 164px; }
  .plan-speed { font-size: 96px; color: var(--navy); left: 163px; }
  .plan-unit { font-size: 42px; color: var(--navy); line-height: 0.86; left: 281px; }
  .plan-unit small { display: block; font-size: 22px; line-height: 1; margin-top: 2px; }

  .premium-price { top: 426px; }
  .premium-term { top: 502px; }
  .premium-speed { top: 557px; }
  .premium-unit { top: 568px; }
  .basic-price { top: 783px; }
  .basic-term { top: 860px; }
  .basic-speed { top: 914px; }
  .basic-unit { top: 924px; }

  .offer-free { left: 480px; top: 390px; font-size: 122px; color: var(--red); }
  .offer-items { left: 672px; top: 397px; font-size: 53px; color: var(--red); line-height: 0.9; }
  .offer-bar {
    position: absolute;
    left: 480px; top: 500px;
    width: 405px; height: 55px;
    background: var(--navy);
    color: var(--white);
    font-size: 27px;
    font-weight: 500;
    letter-spacing: 0.8px;
    display: flex; align-items: center;
    padding-left: 11px;
  }

  .features { position: absolute; left: 0; top: 0; list-style: none; }
  .feature { position: absolute; left: 480px; width: 440px; }
  .feature.speed { top: 600px; }
  .feature.fees { top: 719px; }
  .feature.fiber { top: 848px; }
  .feature-title {
    font-size: 27px; font-weight: 800; color: var(--red);
    line-height: 1.13; letter-spacing: 0.3px;
  }
  .feature-text { font-size: 21px; font-weight: 500; color: var(--body-text); margin-top: 8px; white-space: nowrap; }

  .brand {
    position: absolute;
    left: 580px; top: 1112px;
    display: flex; align-items: center; gap: 10px;
  }
  .brand-dot { width: 14px; height: 14px; border-radius: 50%; background: var(--red); }
  .brand-name { font-size: 31px; font-weight: 700; color: #111a2a; letter-spacing: -0.5px; white-space: nowrap; }
</style>
</head>
<body>
<main class="ad">
  <div class="sky" role="img" aria-label="Night sky with green aurora over snowy pine forest"></div>

  <svg class="waves" width="960" height="1200" viewBox="0 0 960 1200" aria-hidden="true">
    <defs>
      <linearGradient id="band" x1="0" y1="0" x2="1" y2="0">
        <stop offset="0" stop-color="#4cc6de"/>
        <stop offset="1" stop-color="#1a7fc4"/>
      </linearGradient>
      <linearGradient id="floor" x1="0" y1="0" x2="0" y2="1">
        <stop offset="0" stop-color="#ffffff"/>
        <stop offset="1" stop-color="#e3f1f8"/>
      </linearGradient>
    </defs>
    <path d="M0,540 C220,390 560,320 960,345 L960,300 C600,270 300,300 0,470 Z" fill="url(#band)"/>
    <path d="M0,560 C230,405 560,338 960,372 L960,1200 L0,1200 Z" fill="url(#floor)"/>
    <path d="M0,556 C230,400 560,333 960,366" fill="none" stroke="#ffffff" stroke-width="6"/>
    <path d="M250,1200 C520,1050 780,1000 960,990 L960,1010 C790,1020 560,1075 380,1200 Z" fill="url(#band)"/>
    <path d="M380,1200 C560,1075 790,1020 960,1010 L960,1200 Z" fill="#ffffff"/>
  </svg>

  <div class="display headline-internet">Internet</div>
  <div class="display headline-ultra">Ultra</div>
  <div class="display headline-speed">Speed up to</div>
  <div class="display headline-mbps">500 Mbps</div>

  <svg class="plan-ring premium" width="406" height="406" viewBox="0 0 406 406" aria-hidden="true">
    <defs>
      <radialGradient id="ringFill" cx="0.5" cy="0.5" r="0.5">
        <stop offset="0.6" stop-color="#ffffff"/>
        <stop offset="1" stop-color="#cfe9f8"/>
      </radialGradient>
      <linearGradient id="ringStroke" x1="0" y1="0" x2="1" y2="1">
        <stop offset="0" stop-color="#1f4fb5"/>
        <stop offset="0.5" stop-color="#c46be0"/>
        <stop offset="1" stop-color="#3ec8f0"/>
      </linearGradient>
    </defs>
    <circle cx="203" cy="203" r="190" fill="#1a5fb8"/>
    <circle cx="203" cy="203" r="176" fill="url(#ringFill)" stroke="url(#ringStroke)" stroke-width="8"/>
  </svg>
  <svg class="plan-ring basic" width="406" height="406" viewBox="0 0 406 406" aria-hidden="true">
    <circle cx="203" cy="203" r="190" fill="#1a5fb8"/>
    <circle cx="203" cy="203" r="176" fill="url(#ringFill)" stroke="url(#ringStroke)" stroke-width="8"/>
  </svg>

  <div class="display plan-price premium-price">$109<span class="cents">.99</span></div>
  <div class="display plan-term premium-term">Monthly</div>
  <div class="display plan-speed premium-speed">150</div>
  <div class="display plan-unit premium-unit">Mbps<br>Ultra</div>

  <div class="display plan-price basic-price">$89<span class="cents">.99</span></div>
  <div class="display plan-term basic-term">Monthly</div>
  <div class="display plan-speed basic-speed">100</div>
  <div class="display plan-unit basic-unit">Mbps<br>Ultra<small>Basic</small></div>

  <div class="display offer-free">Free</div>
  <div class="display offer-items">Equipment<br>Installation</div>
  <div class="offer-bar">FIRST MONTH OF SERVICE</div>

  <ul class="features">
    <li class="feature speed">
      <h3 class="feature-title">BLAZING FAST<br>SPEEDS</h3>
      <p class="feature-text">Up to 500 Mbps Download Speed</p>
    </li>
    <li class="feature fees">
      <h3 class="feature-title">NO HIDDEN<br>FEES</h3>
      <p class="feature-text">The Price you see is the price you pay</p>
    </li>
    <li class="feature fiber">
      <h3 class="feature-title">FIBER OPTIC INTERNET<br>CONNECTION</h3>
      <p class="feature-text">Enjoy ultra-reliable high-Speed internet</p>
    </li>
  </ul>

  <div class="brand">
    <span class="brand-dot"></span>
    <span class="brand-name">Tallowbrook Media</span>
  </div>
</main>
</body>
</html>
```